Calloway Holdings Website Design

We are a private equity firm based with offices based in Hong Kong, Singapore, London and Paris. Our focus is investments in property development projects, corporate ventures and loans.

We require the development of a new website and you will have to select relevant images from the likes of PixelVaultPics or other stock photo libraries.

We will need a design done for a PC based website and the designer selected with the favored design will also need to produce some concepts for a responsive website.

Target Market(s)

Sophisticated investors looking to invest in high return property development, businesses and mortgages.

Industry/Entity Type

Investment

Number of Pages Required

5+ page

Font styles to use
Serif
Sans Serif

Colors
0255a3
00a990

Requirements
Must have
• Clean modern feel and must portray stability and professionalism.

```html
<!DOCTYPE html>
<html lang="en">
<head>
<meta charset="utf-8">
<title>Calloway Holdings – Services</title>
<link href="https://fonts.googleapis.com/css2?family=Fira+Sans:wght@400;500&family=Open+Sans:wght@400&display=swap" rel="stylesheet">
<style>
:root{
  --navy:#262a5c;
  --navy-deep:#1b1e48;
  --nav-bg:#141518;
  --active:#0b6b12;
  --ink:#2a2a2a;
  --body:#555;
  --footer:#111;
  --footer-deep:#050505;
  --footer-text:#bbb;
  --white:#fff;
}
*{margin:0;padding:0;box-sizing:border-box}
html,body{width:1032px;height:1200px;overflow:hidden;background:var(--white)}
body{position:relative;font-family:"Open Sans",sans-serif;color:var(--body)}
.hero{position:absolute;left:0;top:0;width:1032px;height:234px;
  background:linear-gradient(180deg,#23275a 0%,#3a3d6a 55%,#5a5b7e 100%)}
.brand{position:absolute;left:96px;top:30px;display:flex;align-items:center;gap:8px;
  font-family:"Fira Sans",sans-serif;font-weight:500;font-size:17px;color:var(--white)}
.brand-mark{width:14px;height:14px;background:var(--white)}
.search{position:absolute;left:762px;top:24px;width:174px;height:38px;border:1px solid rgba(255,255,255,.15);
  background:rgba(30,33,75,.6);color:#ccd;font-size:11px;padding:0 14px;display:flex;align-items:center;justify-content:space-between}
.nav{position:absolute;left:96px;top:82px;width:840px;height:48px;background:var(--nav-bg);
  font-family:"Fira Sans",sans-serif;font-weight:500;font-size:10.5px;color:var(--white)}
.nav span{position:absolute;top:0;height:48px;line-height:48px;transform:translateX(-50%)}
.nav .active{background:var(--active);width:114px;text-align:center;transform:none}
.crumbs{position:absolute;left:96px;top:178px;font-family:"Fira Sans",sans-serif;font-size:10.5px;color:var(--white)}
.crumbs .current{color:#c9cbe0}
h1{position:absolute;left:96px;top:266px;font-family:"Fira Sans",sans-serif;font-weight:400;font-size:22px;color:var(--ink)}
.intro{position:absolute;left:96px;top:305px;width:840px;font-size:10.5px;line-height:26px;text-align:justify}
.lead{position:absolute;left:96px;top:367px;font-size:12.5px;color:#333}
.service{position:absolute;width:194px}
.service .photo{height:118px}
.service h2{margin-top:15px;font-family:"Fira Sans",sans-serif;font-weight:500;font-size:12px;line-height:22px;color:var(--ink)}
.outro{position:absolute;left:96px;top:991px;width:840px;font-size:10.5px;line-height:26px;text-align:justify}
.footer{position:absolute;left:0;top:1076px;width:1032px;height:124px;background:var(--footer-deep)}
.footer-links{height:58px;background:var(--footer);display:flex;justify-content:center;align-items:center;
  font-family:"Fira Sans",sans-serif;font-size:10.5px;color:var(--footer-text);gap:9px}
.copy{position:absolute;left:96px;top:84px;font-family:"Fira Sans",sans-serif;font-size:10.5px;color:#999}
.social{position:absolute;left:830px;top:80px;display:flex;gap:6px}
.social i{width:22px;height:22px;border-radius:50%;background:#555;display:block}
</style>
</head>
<body>
<header class="hero" role="img" aria-label="Dark blue photograph of interlocking metal gears"></header>
<div class="brand"><span class="brand-mark"></span>Calloway Holdings</div>
<div class="search">Search
  <svg width="11" height="11" viewBox="0 0 12 12"><circle cx="5" cy="5" r="3.6" fill="none" stroke="#ccd" stroke-width="1.6"/><path d="M7.7 7.7L11 11" stroke="#ccd" stroke-width="1.8"/></svg>
</div>
<nav class="nav">
  <span style="left:51px">HOME</span>
  <span class="active" style="left:101px">SERVICES</span>
  <span style="left:302px">INVESTMENT APPROACH</span>
  <span style="left:461px">CASE STUDIES</span>
  <span style="left:617px">MISSIONS AND VALUES</span>
  <span style="left:761px">CONTACT</span>
</nav>
<div class="crumbs">HOME &nbsp;&nbsp;»&nbsp;&nbsp; <span class="current">SERVICES</span></div>

<h1>SERVICES</h1>
<p class="intro">Calloway Holdings provides independent corporate advisory services in raising capital (equity and debt), strategic merger, acquisition or business sales transactions, implementing management buy-out/buy-in (MBO/MBI) transactions and growth focused advisory services.</p>
<p class="lead">We have established an impressive track record in the following areas:</p>

<div class="service" style="left:96px;top:415px"><div class="photo" role="img" aria-label="Businessman walking towards a sunlit city" style="background:linear-gradient(160deg,#d8cfa8,#8a8060 60%,#4d4736)"></div><h2>Angel Investment</h2></div>
<div class="service" style="left:311px;top:415px"><div class="photo" role="img" aria-label="Aerial view of a city at dusk" style="background:linear-gradient(180deg,#6b6a72,#2d3440 45%,#141a22)"></div><h2>Capital Raisings</h2></div>
<div class="service" style="left:527px;top:415px"><div class="photo" role="img" aria-label="Businessmen shaking hands under office towers" style="background:linear-gradient(150deg,#3b66a8,#7fa7d8 55%,#4a4d58)"></div><h2>Mergers, Acquisitions and Divestments</h2></div>
<div class="service" style="left:742px;top:415px"><div class="photo" role="img" aria-label="Businessman drawing an organisation chart" style="background:linear-gradient(135deg,#dfe7f0,#9fb3cc 60%,#2f4a78)"></div><h2>Capital and Corporate Restructure</h2></div>

<div class="service" style="left:96px;top:606px"><div class="photo" role="img" aria-label="Hands signing documents at a desk" style="background:linear-gradient(160deg,#3a3c52,#c9b9a6 55%,#e8ddc8)"></div><h2>Strategic Business Planning</h2></div>
<div class="service" style="left:311px;top:606px"><div class="photo" role="img" aria-label="Calculator and pen on financial reports" style="background:linear-gradient(150deg,#9cc7e4,#e6eef4 50%,#7b8590)"></div><h2>Financial and Operational Reviews</h2></div>
<div class="service" style="left:527px;top:606px"><div class="photo" role="img" aria-label="Colleagues looking at a tablet" style="background:linear-gradient(135deg,#d7dde2,#8a96a3 55%,#4c5560)"></div><h2>Financial Modelling and Forecasting</h2></div>
<div class="service" style="left:742px;top:606px"><div class="photo" role="img" aria-label="Hand choosing a ticked option" style="background:linear-gradient(135deg,#7c7672,#b9b2ac 50%,#5e5854)"></div><h2>Business Turnaround Advice</h2></div>

<div class="service" style="left:96px;top:806px"><div class="photo" role="img" aria-label="Money bags on a table" style="background:linear-gradient(180deg,#2f6b6a,#447f7c 65%,#5a4237)"></div><h2>Litigation Funding</h2></div>
<div class="service" style="left:311px;top:806px"><div class="photo" role="img" aria-label="Pen and calculator on spreadsheet" style="background:linear-gradient(135deg,#e9ecef,#b6bcc2 60%,#3d5d8a)"></div><h2>Loans and General Funding</h2></div>
<div class="service" style="left:527px;top:806px"><div class="photo" role="img" aria-label="Team meeting around a table" style="background:linear-gradient(150deg,#5d5a56,#a88f76 55%,#3a3836)"></div><h2>Advisors and consultants</h2></div>
<div class="service" style="left:742px;top:806px"><div class="photo" role="img" aria-label="Businessmen working on a glass chart" style="background:linear-gradient(135deg,#c5ccd6,#6f7c92 55%,#2d3448)"></div><h2>Hands-on operating approach</h2></div>

<p class="outro">Our success is directly related to the calibre of its people who hold a wealth of both national and international experience with a diverse combination of strategic, operational and financial skills.</p>

<footer class="footer">
  <div class="footer-links">
    <span>Home</span>|<span>Services</span>|<span>Investment Approach</span>|<span>Case Studies</span>|<span>Missions and Values</span>|<span>Contact us</span>|<span>What people say</span>|<span>Legal disclaimer</span>
  </div>
  <div class="copy">Copyright © 2016 Calloway Holdings. All rights reserved</div>
  <div class="social"><i></i><i></i><i></i><i></i></div>
</footer>
</body>
</html>
```